Harbor Logistics Business card and letterhead
Professional business card
Professional
Calvin Marsh
Director of Operations
4538 E 61st Pl
Maple Grove, KS 66417-3814
cmarsh@harborlogisticsco.example
http://www.harborlogisticsco.example
Looking for something clean, professional, and simple. Fonts are optional, just flow with fonts in logo
On the back we would like the mission of "Moving Every Load Forward" printed in some design. We would like the background to be a solid design from a logo color with white writing
This is our corporate logo

```html
<!DOCTYPE html>
<html lang="en">
<head>
<meta charset="utf-8">
<title>Harbor Logistics Stationery</title>
<link href="https://fonts.googleapis.com/css2?family=Michroma&family=Open+Sans:wght@400;600&display=swap" rel="stylesheet">
<style>
  :root {
    --green-deep: #0b5e2a;
    --green: #1f8b3a;
    --green-soft: #4fae3c;
    --ink: #0d0d0d;
    --brand-blue: #1d3d7a;
    --text-green: #2f8f3e;
    --paper: #ffffff;
    --white: #ffffff;
  }
  * { margin: 0; padding: 0; box-sizing: border-box; }
  html, body { width: 1200px; height: 988px; overflow: hidden; background: var(--paper); }
  body { position: relative; font-family: "Open Sans", Arial, sans-serif; }

  .sheet { position: absolute; background: var(--paper); box-shadow: 0 1px 4px rgba(0,0,0,.25); overflow: hidden; }
  .header-band { position: absolute; left: 0; top: 0; width: 100%; background: linear-gradient(90deg, var(--green-deep), var(--green) 60%, var(--green-soft)); border-bottom: solid var(--ink); }

  .brand { position: absolute; display: flex; flex-direction: column; align-items: flex-start; }
  .brand-dot { border-radius: 50%; background: var(--brand-blue); }
  .brand-name { font-family: "Michroma", Arial, sans-serif; color: var(--brand-blue); letter-spacing: .04em; line-height: 1.15; white-space: nowrap; }

  .letterhead { left: 14px; top: 12px; width: 864px; height: 955px; }
  .letterhead .header-band { height: 64px; border-bottom-width: 10px; }
  .letterhead .brand { left: 46px; top: 88px; }
  .letterhead .brand-dot { width: 88px; height: 88px; margin-bottom: 10px; }
  .letterhead .brand-name { font-size: 24px; }
  .letterhead .footer { position: absolute; left: 50px; top: 877px; color: var(--text-green); font-size: 13px; line-height: 1.45; }

  .envelope-flap { left: 14px; top: 318px; width: 864px; height: 138px; background: var(--green-deep); }

  .envelope { left: 14px; top: 474px; width: 864px; height: 366px; }
  .envelope .header-band { height: 44px; border-bottom-width: 8px; }
  .envelope .brand { left: 42px; top: 84px; }
  .envelope .brand-dot { width: 66px; height: 66px; margin-bottom: 8px; }
  .envelope .brand-name { font-size: 19px; }
  .envelope .return { position: absolute; left: 48px; top: 292px; color: var(--text-green); font-size: 13px; line-height: 1.45; }

  .card-front { left: 895px; top: 459px; width: 300px; height: 195px; }
  .card-front .header-band { height: 26px; border-bottom-width: 5px; }
  .card-front .brand { left: 16px; top: 48px; }
  .card-front .brand-dot { width: 34px; height: 34px; margin-bottom: 4px; }
  .card-front .brand-name { font-size: 10px; }
  .card-front .person { position: absolute; right: 20px; top: 60px; text-align: center; color: var(--text-green); }
  .card-front .person .name { font-size: 11px; font-weight: 600; }
  .card-front .person .role { font-size: 7px; }
  .card-front .details { position: absolute; left: 16px; top: 110px; font-size: 6.5px; line-height: 1.4; color: var(--text-green); }

  .card-back { left: 895px; top: 673px; width: 300px; height: 232px; background: var(--green-deep); }
  .card-back .mission { position: absolute; left: 0; right: 0; top: 160px; text-align: center; color: var(--white); font-size: 13px; font-style: italic; }
</style>
</head>
<body>

<section class="sheet letterhead">
  <div class="header-band" role="img" aria-label="Green header band"></div>
  <div class="brand"><span class="brand-dot"></span><span class="brand-name">HARBOR LOGISTICS</span></div>
  <div class="footer">
    4538 E 61st Pl  Maple Grove, KS 66417-3814<br>
    Phone (785) 555-0142  |  Cell (785) 555-0187<br>
    www.harborlogisticsco.example
  </div>
</section>

<section class="sheet envelope-flap" role="img" aria-label="Solid green envelope flap"></section>

<section class="sheet envelope">
  <div class="header-band" role="img" aria-label="Green header band"></div>
  <div class="brand"><span class="brand-dot"></span><span class="brand-name">HARBOR LOGISTICS</span></div>
  <div class="return">4538 E 61st Pl<br>Maple Grove, KS 66417-3814</div>
</section>

<section class="sheet card-front">
  <div class="header-band" role="img" aria-label="Green header band"></div>
  <div class="brand"><span class="brand-dot"></span><span class="brand-name">HARBOR LOGISTICS</span></div>
  <div class="person"><div class="name">Calvin Marsh</div><div class="role">Director of Operations</div></div>
  <div class="details">
    4538 E 61st Pl<br>
    Maple Grove, KS 66417-3814<br>
    Phone (785) 555-0142<br>
    Cell (785) 555-0187<br>
    Fax (785) 555-0143<br>
    cmarsh@harborlogisticsco.example<br>
    www.harborlogisticsco.example
  </div>
</section>

<section class="sheet card-back">
  <p class="mission">"Moving Every Load Forward"</p>
</section>

</body>
</html>
```